Business Consulting Business Card

professional business card with basic information (1) First and Last name (2) email address, (3) phone number, (4) website.

```html
<!DOCTYPE html>
<html lang="en">
<head>
<meta charset="utf-8">
<title>Tide Hollow – Business Card</title>
<link href="https://fonts.googleapis.com/css2?family=Arimo:wght@400;500&family=Montserrat:wght@400&display=swap" rel="stylesheet">
<style>
  :root {
    --backdrop: #0b4a63;
    --navy: #062238;
    --paper: #f6f7f8;
    --ink: #0d1c2c;
    --aqua: #34b3c9;
    --aqua-light: #4fc8cf;
    --aqua-deep: #2a8fb8;
    --white: #ffffff;
  }
  * { box-sizing: border-box; margin: 0; padding: 0; }
  html, body { width: 1200px; height: 900px; overflow: hidden; }
  body {
    background: var(--backdrop);
    display: flex;
    align-items: center;
    justify-content: center;
    gap: 60px;
  }
  .card {
    width: 525px;
    height: 300px;
    border-radius: 4px;
    box-shadow: 0 18px 40px rgba(0, 20, 35, 0.35);
    position: relative;
    overflow: hidden;
  }
  .card-front {
    background: var(--navy);
    display: flex;
    align-items: center;
    justify-content: center;
    gap: 18px;
  }
  .brand-mark {
    width: 44px;
    height: 44px;
    border-radius: 50%;
    background: var(--aqua);
  }
  .brand-name {
    font-family: "Montserrat", sans-serif;
    font-weight: 400;
    font-size: 30px;
    letter-spacing: 0.32em;
    color: var(--white);
  }
  .card-back {
    background: radial-gradient(ellipse at 55% 45%, var(--white) 0%, var(--paper) 60%, #e6e8ea 100%);
    display: flex;
    align-items: center;
    justify-content: center;
    gap: 16px;
    font-family: "Arimo", sans-serif;
  }
  .identity { text-align: right; }
  .person-name {
    font-size: 30px;
    font-weight: 400;
    letter-spacing: -0.04em;
    color: var(--ink);
    line-height: 1;
  }
  .person-role {
    font-size: 16px;
    color: var(--aqua-deep);
    margin-top: 3px;
  }
  .icon-strip {
    width: 46px;
    height: 104px;
    border-radius: 9px;
    background: linear-gradient(180deg, var(--aqua-light), var(--aqua-deep));
    display: flex;
    flex-direction: column;
    align-items: center;
    justify-content: space-around;
    padding: 10px 0;
  }
  .icon-strip .divider { width: 22px; height: 2px; background: var(--white); }
  .contact-list {
    list-style: none;
    font-size: 14px;
    color: var(--ink);
    line-height: 1.25;
  }
  .contact-list .gap { margin-top: 12px; }
</style>
</head>
<body>
  <section class="card card-front" aria-label="Card front">
    <span class="brand-mark" aria-hidden="true"></span>
    <span class="brand-name">TIDE HOLLOW</span>
  </section>

  <section class="card card-back" aria-label="Card back">
    <div class="identity">
      <p class="person-name">YOUR NAME</p>
      <p class="person-role">Solution Manager</p>
    </div>
    <div class="icon-strip" aria-hidden="true">
      <svg width="20" height="20" viewBox="0 0 24 24"><path fill="#fff" d="M6.6 10.8a15.1 15.1 0 0 0 6.6 6.6l2.2-2.2a1 1 0 0 1 1-.25 11.4 11.4 0 0 0 3.6.57 1 1 0 0 1 1 1V20a1 1 0 0 1-1 1A17 17 0 0 1 3 4a1 1 0 0 1 1-1h3.5a1 1 0 0 1 1 1c0 1.25.2 2.45.57 3.57a1 1 0 0 1-.25 1z"/></svg>
      <span class="divider"></span>
      <svg width="22" height="22" viewBox="0 0 24 24" fill="none" stroke="#fff" stroke-width="1.8"><circle cx="12" cy="12" r="9"/><ellipse cx="12" cy="12" rx="4" ry="9"/><path d="M3 12h18M5 7h14M5 17h14"/></svg>
    </div>
    <ul class="contact-list">
      <li>123-456-7890</li>
      <li>123-456-7890</li>
      <li class="gap">name@email.com</li>
      <li>www.website.com</li>
    </ul>
  </section>
</body>
</html>
```